New counselling and hypnotherapy business

I'd like a flyer which is relevant to people who want support and to improve their wellbeing which follows the same theme as my website: http://wrenlowtherapy.sitepailo.com
And emphasise that whatever the area of concern, development or growth and I can tailor my knowledge and skills to help.

I'd like to use the same logo and my emphasis is to draw the audience in...therapy and counselling is for people who are "stuck" and having a difficult time...it can also be useful has a personal development tool.

Hypnotherapy

```html
<!DOCTYPE html>
<html lang="en">
<head>
<meta charset="utf-8">
<title>Wrenlow Counselling &amp; Hypnotherapy – Flyer</title>
<link rel="stylesheet" href="https://fonts.googleapis.com/css2?family=Comfortaa:wght@400;600;700&display=swap">
<style>
  :root {
    --purple: #6b2dbb;
    --purple-deep: #5a2a9c;
    --green: #3cf20f;
    --white: #ffffff;
  }
  * { margin: 0; padding: 0; box-sizing: border-box; }
  html, body { width: 848px; height: 1200px; overflow: hidden; background: var(--white); }
  .flyer {
    position: relative;
    width: 848px;
    height: 1200px;
    overflow: hidden;
    background: var(--white);
    font-family: "Comfortaa", sans-serif;
    color: var(--white);
  }
  .wave { position: absolute; left: 0; top: 0; width: 848px; height: 1200px; }
  .brand {
    position: absolute;
    left: 88px;
    top: 186px;
    color: var(--purple-deep);
    font-family: "Comfortaa", sans-serif;
    font-weight: 600;
    line-height: 1.1;
  }
  .brand-name { display: block; font-size: 40px; letter-spacing: 1px; }
  .brand-line { display: block; font-size: 29px; }
  .quote {
    position: absolute;
    left: 30px;
    top: 452px;
    width: 788px;
    text-align: center;
    font-size: 26px;
    font-weight: 600;
    line-height: 44px;
    letter-spacing: 0.3px;
  }
  .quote-line { display: block; white-space: nowrap; }
  .topic { position: absolute; width: 400px; }
  .topic h2 {
    font-size: 29px;
    font-weight: 700;
    line-height: 34px;
    margin-bottom: 4px;
  }
  .topic p {
    font-size: 17px;
    line-height: 26.5px;
    font-weight: 400;
  }
  .topic--clarify { left: 17px; top: 660px; }
  .topic--explore { left: 17px; top: 906px; }
  .topic--growth { left: 442px; top: 662px; }
  .topic--behaviour { left: 442px; top: 946px; }
  .footer-band {
    position: absolute;
    left: 0;
    top: 1131px;
    width: 848px;
    height: 14px;
    background: var(--green);
  }
  .contact {
    position: absolute;
    left: 0;
    top: 1158px;
    width: 848px;
    text-align: center;
    color: var(--purple);
    font-size: 18.5px;
    font-weight: 400;
  }
</style>
</head>
<body>
<main class="flyer">
  <svg class="wave" viewBox="0 0 848 1200" aria-hidden="true">
    <path d="M0 300 C130 304 260 396 440 396 C610 396 710 268 848 205 L848 1131 L0 1131 Z" fill="var(--green)"/>
    <path d="M0 322 C130 326 260 418 440 418 C610 418 710 290 848 227 L848 1131 L0 1131 Z" fill="var(--purple)"/>
  </svg>

  <div class="brand">
    <span class="brand-name">Wrenlow</span>
    <span class="brand-line">Counselling &amp;</span>
    <span class="brand-line">Hypnotherapy</span>
  </div>

  <p class="quote">
    <span class="quote-line">“Sometimes when I'm in the boat alone, it doesn't</span>
    <span class="quote-line">feel like I have any oars. … up out of the fog, I can</span>
    <span class="quote-line">see your harbour light somewhere out there,</span>
    <span class="quote-line">guiding me in.”</span>
  </p>

  <section class="topic topic--clarify">
    <h2>Clarify</h2>
    <p>I want to understand more about my relationship with others. I'm not sure how to cope with my grief and loss. I feel anxious and scared and I'm not sure why. I'm not sure how to relax.</p>
  </section>

  <section class="topic topic--explore">
    <h2>Explore</h2>
    <p>There's something I want to explore and make sense of. I'm feeling really down, low and depressed and I feel stuck. To me the world just looks like a fog. I'd like to have some support and somebody to listen. I feel overwhelmed.</p>
  </section>

  <section class="topic topic--growth">
    <h2>Growth and development</h2>
    <p>I want to improve my level of confidence and self esteem. I want to personally gain a greater self awareness. I want to improve communication with my manager and my team. I want to move on to something else.</p>
  </section>

  <section class="topic topic--behaviour">
    <h2>Behaviour change</h2>
    <p>I want to stop smoking. I want to feel less anxious. I want to stop harming myself. I want to stop the phobia I have.</p>
  </section>

  <div class="footer-band"></div>
  <p class="contact">www.wrenlowtherapy.sitepailo.com | 07700 900514 | wrenlowtherapy@mailbox.co.uk</p>
</main>
</body>
</html>
```